Saucy Velvet Kittenz Business Card

We need business cards designed for our consultants to use and hand out to customers.
We are an Adult party plan company (like Crispaboxa but sex toys and lingerie)
We would like bright colours pinks, purples.
The cards need our logo
Space for the reps phone number email address and name.
We need our website on it www.saucyvelvetkittens.com.au

```html
<!DOCTYPE html>
<html lang="en">
<head>
<meta charset="utf-8">
<title>Saucy Velvet Kittenz – Business Card</title>
<link rel="stylesheet" href="https://fonts.googleapis.com/css2?family=Arimo:ital,wght@0,700;1,700&family=Fira+Sans:wght@700&display=swap">
<style>
  :root {
    --paper: #ffffff;
    --brand-pink: #ec008c;
    --brand-purple: #92278f;
    --brand-red: #c1272d;
    --web-magenta: #b8176f;
    --ink: #111111;
    --muted: #808285;
  }
  html, body {
    margin: 0;
    padding: 0;
    overflow: hidden;
    background: var(--paper);
  }
  .card {
    position: relative;
    width: 1200px;
    height: 686px;
    background: var(--paper);
    overflow: hidden;
  }
  .band-pink {
    position: absolute;
    left: 0; top: 118px;
    width: 1200px; height: 63px;
    background: var(--brand-pink);
  }
  .band-purple {
    position: absolute;
    left: 0; top: 192px;
    width: 1200px; height: 18px;
    background: var(--brand-purple);
  }
  .brand-mark {
    position: absolute;
    left: 118px; top: 110px;
    width: 180px; height: 180px;
  }
  .brand-name {
    position: absolute;
    left: 261px; top: 118px;
    height: 63px;
    line-height: 63px;
    margin: 0;
    font-family: "Fira Sans", sans-serif;
    font-weight: 700;
    font-size: 50px;
    color: var(--paper);
    white-space: nowrap;
  }
  .rep-name {
    position: absolute;
    left: 377px; top: 248px;
    margin: 0;
    font-family: "Arimo", sans-serif;
    font-style: italic;
    font-weight: 700;
    font-size: 46px;
    color: var(--ink);
  }
  .rep-phone {
    position: absolute;
    left: 356px; top: 316px;
    display: flex;
    align-items: center;
    gap: 14px;
    font-family: "Arimo", sans-serif;
    font-weight: 700;
    font-size: 52px;
    color: var(--muted);
  }
  .phone-icon { width: 44px; height: 70px; }
  .rep-email {
    position: absolute;
    left: 357px; top: 413px;
    font-family: "Arimo", sans-serif;
    font-weight: 700;
    font-size: 39px;
    color: var(--muted);
  }
  .website {
    position: absolute;
    right: 21px; top: 614px;
    font-family: "Fira Sans", sans-serif;
    font-weight: 700;
    font-size: 43px;
    color: var(--web-magenta);
  }
</style>
</head>
<body>
  <div class="card">
    <div class="band-pink"></div>
    <div class="band-purple"></div>

    <svg class="brand-mark" viewBox="0 0 180 180" role="img" aria-label="Saucy Velvet Kittenz brand mark">
      <circle cx="90" cy="90" r="86" fill="var(--brand-red)"/>
    </svg>

    <h1 class="brand-name">Saucy Velvet Kittenz</h1>

    <p class="rep-name">Jamie Sample</p>

    <div class="rep-phone">
      <svg class="phone-icon" viewBox="0 0 44 70" aria-hidden="true">
        <path d="M14 4 h10 v16 h-8 c-4 8 -4 22 0 30 h8 v16 h-10 C2 58 -2 14 14 4 Z" fill="var(--brand-red)"/>
        <rect x="26" y="4" width="6" height="16" rx="2" fill="var(--brand-red)"/>
        <rect x="26" y="50" width="6" height="16" rx="2" fill="var(--brand-red)"/>
      </svg>
      <span>0400 1234</span>
    </div>

    <div class="rep-email">jamie@saucyvelvetkittens.com</div>

    <div class="website">www.saucyvelvetkittens.com.au</div>
  </div>
</body>
</html>
```